Marine Electronics Manufacturer needs an infographic for aquaculture related product

Dissolved CO2 Removal For Fish Transport Infographic

Background
When fish breathe underwater they pass water over their gills and absorb dissolved oxygen (O2) from the water and at the same time release CO2 into the water as dissolved gas. The process is similar to humans, with the exception that the O2 and CO2 is absorbed from the water rather than being breathed in as a gas. When live fish are transported by road, rail or air they are typically packed into large sealed bins with water and one of the challenges is to be able to fit enough fish onto a bin to make it commercially viable, while maintaining the health and welfare of the fish. And the more fish you have the more CO2 will be released into the water, which often contributes to high mortality rates and poor health outcomes for the fish. So the removal of the CO2 from the water during transport is often essential to being able to achieve the dual outcomes of market viability and healthy fish.

Infographic Requirements
The infographic needs to illustrate clearly the process described below for the removal of dissolved CO2 from the water in sealed live fish transport bins. Also see the attached image that provides a graphical description of the key processes.

- Live fish are transported in sealed bins with water
- Fish take in O2 from the water and at the same time expel CO2 into the water as part of respiration.
- Keeping CO2 levels in the in the water low improves the survival of the fish results in better health outcomes.
- The process selectively removes CO2 from the water using a gas specific membrane that water is pumped through
- There is a sweep gas (air) from outside the bin is pumped through the membrane in the reverse direction to the water that takes the CO2 removed from the water and expels it outside the bin.
- The water is continuously re-circulating through the system and the air is always fresh from outside the system with no re-circulation.

Please include:

- Option for Harbor Crest logo to be included
- Harbor crest URL harborcrest-example.com.au
- Please use logo colours for guidance on the colour scheme of overall graphic.

```html
<!DOCTYPE html>
<html lang="en">
<head>
<meta charset="utf-8">
<title>Harbor Crest – Dissolved CO₂ Removal</title>
<link rel="stylesheet" href="https://fonts.googleapis.com/css2?family=Jost:wght@400;500&display=swap">
<style>
  :root {
    --page-bg: #ededed;
    --card-bg: #ffffff;
    --brand-blue: #1e9bd7;
    --water-top: #29a9e1;
    --water-bottom: #2191c4;
    --water-deep: #1c7fb1;
    --air-out: #f0545a;
    --air-in: #3ddc8a;
    --ink: #3a3f44;
    --white: #ffffff;
  }
  html, body {
    margin: 0;
    padding: 0;
    width: 1200px;
    height: 827px;
    overflow: hidden;
    background: var(--page-bg);
  }
  .infographic {
    position: absolute;
    left: 30px;
    top: 93px;
    width: 1140px;
    height: 641px;
    background: var(--card-bg);
  }
  .infographic svg {
    display: block;
    width: 1140px;
    height: 641px;
    font-family: "Jost", sans-serif;
  }
  .brand-name { fill: var(--brand-blue); font-size: 36px; font-weight: 500; }
  .air-out-label { fill: var(--air-out); font-size: 23px; font-weight: 400; }
  .air-in-label { fill: var(--air-in); font-size: 23px; font-weight: 400; }
  .air-note { fill: var(--ink); font-size: 16px; letter-spacing: 0.5px; }
  .site-url { fill: var(--ink); font-size: 20px; font-weight: 500; letter-spacing: 0.5px; }
  .water-label { fill: var(--white); font-size: 23px; font-weight: 400; }
  .water-note { fill: var(--white); font-size: 16px; }
</style>
</head>
<body>
<main class="infographic">
  <svg viewBox="0 0 1425 801" xmlns="http://www.w3.org/2000/svg">
    <defs>
      <linearGradient id="water-fill" x1="0" y1="0" x2="0" y2="1">
        <stop offset="0" stop-color="#29a9e1"/>
        <stop offset="1" stop-color="#2191c4"/>
      </linearGradient>
      <linearGradient id="membrane-fill" x1="0" y1="0" x2="0" y2="1">
        <stop offset="0" stop-color="#ffffff"/>
        <stop offset="0.75" stop-color="#c6e8f8"/>
        <stop offset="0.92" stop-color="#a6dbf4"/>
        <stop offset="1" stop-color="#d6effb"/>
      </linearGradient>
      <radialGradient id="school-fill" cx="0.5" cy="0.5" r="0.5">
        <stop offset="0" stop-color="#1c7fb1" stop-opacity="0.55"/>
        <stop offset="0.6" stop-color="#1c7fb1" stop-opacity="0.3"/>
        <stop offset="1" stop-color="#1c7fb1" stop-opacity="0"/>
      </radialGradient>
    </defs>

    <!-- header -->
    <g class="brand">
      <rect x="71" y="66" width="26" height="26" rx="4" fill="var(--brand-blue)"/>
      <text class="brand-name" x="108" y="92">Harbor Crest</text>
    </g>
    <text class="air-out-label" x="461" y="80" text-anchor="middle">AIR OUT</text>
    <text class="air-note" x="461" y="103" text-anchor="middle">(CO₂ RICH)</text>
    <text class="air-in-label" x="963" y="80" text-anchor="middle">AIR IN</text>
    <text class="air-note" x="963" y="103" text-anchor="middle">(FRESH)</text>
    <text class="site-url" x="1320" y="142" text-anchor="end">harborcrest-example.com.au</text>
    <rect x="1330" y="126" width="18" height="18" rx="4" fill="var(--brand-blue)"/>

    <!-- water body -->
    <path d="M0 801 V247 Q0 167 80 167 H1345 Q1425 167 1425 247 V801 Z" fill="url(#water-fill)"/>

    <!-- fish artwork areas -->
    <rect class="fish-school" x="520" y="212" width="240" height="160" fill="url(#school-fill)"
          role="img" aria-label="School of live fish breathing: taking in O2 from the water and releasing CO2 into it"/>
    <rect class="fish-school" x="110" y="330" width="220" height="200" fill="url(#school-fill)"
          role="img" aria-label="Live fish swimming in the sealed transport bin"/>
    <rect class="fish-school" x="1170" y="250" width="200" height="260" fill="url(#school-fill)"
          role="img" aria-label="Live fish swimming in the sealed transport bin"/>

    <!-- sealed bin label -->
    <path d="M93 240 a17 17 0 0 1 17 17 c0 11 -17 26 -17 26 s-17 -15 -17 -26 a17 17 0 0 1 17 -17 z" fill="var(--white)"/>
    <circle cx="93" cy="256" r="6" fill="var(--water-top)"/>
    <text class="water-label" x="126" y="256">SEALED FISH</text>
    <text class="water-label" x="126" y="283">TRANSPORT BIN</text>

    <!-- respiration arrows -->
    <g fill="var(--white)">
      <rect x="758" y="234" width="4" height="27"/>
      <path d="M752 236 L760 223 L768 236 Z"/>
      <rect x="758" y="322" width="4" height="27"/>
      <path d="M752 324 L760 311 L768 324 Z"/>
    </g>
    <text class="water-label" x="773" y="262">CO₂</text>
    <text class="water-label" x="773" y="350">O₂</text>

    <!-- membrane module -->
    <path d="M334 437 H427 V398 Q427 383 442 383 H481 Q496 383 496 398 V437 H929 V398 Q929 383 944 383 H983 Q998 383 998 398 V437 H1091 Q1121 437 1121 467 V635 Q1121 665 1091 665 H334 Q304 665 304 635 V467 Q304 437 334 437 Z" fill="url(#membrane-fill)"/>
    <line x1="324" y1="551" x2="1100" y2="551" stroke="var(--water-deep)" stroke-width="3" stroke-dasharray="18 14"/>

    <!-- air flow -->
    <line x1="461" y1="509" x2="461" y2="134" stroke="var(--air-out)" stroke-width="3"/>
    <path d="M454 136 L461 121 L468 136 Z" fill="var(--air-out)"/>
    <line x1="486" y1="509" x2="713" y2="509" stroke="var(--air-out)" stroke-width="3" stroke-dasharray="22 12"/>
    <path d="M488 502 L473 509 L488 516 Z" fill="var(--air-out)"/>

    <line x1="963" y1="121" x2="963" y2="480" stroke="var(--air-in)" stroke-width="3"/>
    <path d="M956 479 L963 494 L970 479 Z" fill="var(--air-in)"/>
    <line x1="738" y1="509" x2="963" y2="509" stroke="var(--air-in)" stroke-width="3" stroke-dasharray="22 12"/>
    <path d="M740 502 L725 509 L740 516 Z" fill="var(--air-in)"/>

    <!-- water flow -->
    <line x1="77" y1="551" x2="278" y2="551" stroke="var(--white)" stroke-width="3"/>
    <path d="M276 544 L291 551 L276 558 Z" fill="var(--white)"/>
    <text class="water-label" x="77" y="587">H₂O IN</text>
    <text class="water-note" x="77" y="610">(HIGH CO₂)</text>

    <line x1="1348" y1="551" x2="1147" y2="551" stroke="var(--white)" stroke-width="3"/>
    <path d="M1149 544 L1134 551 L1149 558 Z" fill="var(--white)"/>
    <text class="water-label" x="1348" y="587" text-anchor="end">H₂O OUT</text>
    <text class="water-note" x="1348" y="610" text-anchor="end">(LOW CO₂)</text>

    <!-- membrane label -->
    <text class="water-label" x="1071" y="707" text-anchor="end">CO₂ GAS SPECIFIC</text>
    <text class="water-label" x="1071" y="734" text-anchor="end">MEMBRANE</text>
    <path d="M1104 690 C1097 702 1086 711 1086 721 a18 18 0 0 0 36 0 C1122 711 1111 702 1104 690 Z" fill="var(--white)"/>
    <circle cx="1104" cy="719" r="6" fill="var(--water-bottom)"/>
  </svg>
</main>
</body>
</html>
```